Business card for a shipping supplies business

Needing a business card design. Please see the logo. The logo with the white font should be used if there is a dark background.

We are looking for the following info on the card. Please see the sample info. We will need the info to be changed with a few different employee names and info but all will use the same template.

Business Name: The Crate Heron
Employee Name : Marcus Delaney
Position: Account Manager
Address: 4827 W. Ridge 418 S.
Fort Worth, TX 73948
email: Marcus@thecrateheron.example
telephone: 855-619-2740 x 207
website: www.getparcelkits.example

Target Market(s)

Businesses who ship products for online sales

Industry/Entity Type

Cardboard

Contact Information for Business Card

Name, title, address, website, logo, telephone number

Font styles to use
Sans Serif

Colors
EE7325
F08F49
F5BC92
FAE3D3
FDF4ED

Requirements
Must have
• Logo on back of card. Clean look, just logo, website address

```html
<!DOCTYPE html>
<html lang="en">
<head>
<meta charset="utf-8">
<title>The Crate Heron — Business Card</title>
<link href="https://fonts.googleapis.com/css2?family=Exo+2:wght@400;500;600&display=swap" rel="stylesheet">
<style>
  :root {
    --page: #8b8f90;
    --card: #1b1b1b;
    --card-edge: #141414;
    --orange: #d35f27;
    --orange-light: #ee7325;
    --tan: #c4906a;
    --white: #ffffff;
    --text: #f2f2f2;
  }
  * { margin: 0; padding: 0; box-sizing: border-box; }
  html, body { width: 1200px; height: 928px; overflow: hidden; }
  body {
    background: var(--page);
    font-family: "Exo 2", sans-serif;
    color: var(--text);
    position: relative;
  }
  .card {
    position: absolute;
    background: linear-gradient(135deg, #202020, var(--card-edge));
    border-radius: 16px;
    overflow: hidden;
  }
  .card--front { left: 267px; top: 59px; width: 670px; height: 382px; }
  .card--back  { left: 264px; top: 484px; width: 676px; height: 386px; }

  /* Front */
  .brand {
    position: absolute; left: 0; right: 0; top: 232px;
    display: flex; justify-content: center; align-items: center; gap: 12px;
  }
  .brand__mark { width: 30px; height: 30px; background: var(--orange-light); }
  .brand__name { font-size: 32px; font-weight: 600; color: var(--white); letter-spacing: 1px; }
  .front-web {
    position: absolute; left: 0; right: 0; top: 338px;
    text-align: center; font-size: 14px; font-weight: 600; letter-spacing: 2px; color: var(--white);
  }
  .front-web span { color: var(--orange-light); }

  /* Back */
  .person { position: absolute; left: 41px; top: 52px; }
  .person__name { font-size: 26px; font-weight: 600; color: var(--orange-light); line-height: 1.1; }
  .person__title { font-size: 16px; margin-top: 4px; }
  .address { position: absolute; left: 41px; top: 162px; font-size: 16px; line-height: 27px; letter-spacing: .3px; }
  .contacts { position: absolute; left: 41px; top: 253px; list-style: none; font-size: 16.5px; letter-spacing: .4px; }
  .contacts li { display: flex; align-items: center; gap: 8px; height: 27px; }
  .contacts svg { width: 14px; height: 14px; fill: var(--orange); flex: none; }
  .mark-area {
    position: absolute; left: 440px; top: 70px; width: 230px; height: 240px;
    display: flex; align-items: center; justify-content: center;
  }
  .mark-area__shape {
    width: 170px; height: 170px; background: var(--tan);
    border: 6px solid #111; outline: 3px solid var(--orange);
  }
  .band { position: absolute; left: 0; bottom: 0; width: 676px; height: 34px; }
</style>
</head>
<body>
  <section class="card card--front" aria-label="Card front">
    <div class="brand">
      <span class="brand__mark"></span>
      <span class="brand__name">The Crate Heron</span>
    </div>
    <p class="front-web">www.<span>getparcelkits</span>.example</p>
  </section>

  <section class="card card--back" aria-label="Card back">
    <div class="person">
      <h1 class="person__name">Marcus Delaney</h1>
      <p class="person__title">Account Manager</p>
    </div>
    <p class="address">4827 W. Ridge 418 S.<br>Fort Worth, TX 73948</p>
    <ul class="contacts">
      <li>
        <svg viewBox="0 0 24 24"><path d="M6.6 10.8a15 15 0 0 0 6.6 6.6l2.2-2.2a1 1 0 0 1 1-.25 11.4 11.4 0 0 0 3.6.6 1 1 0 0 1 1 1V20a1 1 0 0 1-1 1A17 17 0 0 1 3 4a1 1 0 0 1 1-1h3.5a1 1 0 0 1 1 1c0 1.25.2 2.45.6 3.6a1 1 0 0 1-.25 1z"/></svg>
        855-619-2740 x 207
      </li>
      <li>
        <svg viewBox="0 0 24 24"><path d="M2 5h20v14H2z M2 6l10 7 10-7" fill="var(--orange)"/><path d="M3 6.5l9 6.3 9-6.3" fill="none" stroke="#1b1b1b" stroke-width="1.8"/></svg>
        Marcus@thecrateheron.example
      </li>
      <li>
        <svg viewBox="0 0 24 24"><circle cx="12" cy="12" r="10"/><path d="M2 12h20M12 2c3 3 3 17 0 20M12 2c-3 3-3 17 0 20" fill="none" stroke="#1b1b1b" stroke-width="1.5"/></svg>
        www.getparcelkits.example
      </li>
    </ul>
    <div class="mark-area" role="img" aria-label="Company mark placeholder">
      <div class="mark-area__shape"></div>
    </div>
    <svg class="band" viewBox="0 0 676 34" preserveAspectRatio="none" aria-hidden="true">
      <polygon points="0,0 330,0 344,17 330,34 0,34" fill="var(--orange)"/>
      <polygon points="349,0 676,0 676,34 349,34 363,17" fill="var(--white)"/>
    </svg>
  </section>
</body>
</html>
```